Construction business card

I need a new business card, they can connect with my logo, brand.
What we do is residential house , design and build
I like: Navy blue / black
I attached our logo, brand,
and, some idea for business card.

```html
<!DOCTYPE html>
<html lang="en">
<head>
<meta charset="utf-8">
<title>Orbit Building Co – Business Card</title>
<link rel="stylesheet" href="https://fonts.googleapis.com/css2?family=Poppins:wght@400;700&display=swap">
<style>
  :root {
    --backdrop: #1d1d1f;
    --card-blue: #2f6db5;
    --card-blue-deep: #245a98;
    --ink-white: #ffffff;
  }
  * { margin: 0; padding: 0; box-sizing: border-box; }
  html, body {
    width: 1200px;
    height: 900px;
    overflow: hidden;
    background: var(--backdrop);
    font-family: "Poppins", sans-serif;
  }
  .canvas {
    position: relative;
    width: 1200px;
    height: 900px;
  }
  .card {
    position: absolute;
    width: 580px;
    height: 330px;
    background: var(--card-blue);
    border-radius: 3px;
  }
  .card--front { left: 110px; top: 100px; }
  .card--back { left: 510px; top: 470px; }

  .brand-name {
    position: absolute;
    font-weight: 700;
    letter-spacing: 1px;
    white-space: nowrap;
    text-transform: uppercase;
  }
  .card--front .brand-name {
    left: 0; right: 0; top: 140px;
    text-align: center;
    font-size: 40px;
    color: var(--ink-white);
  }
  .card--back .brand-name {
    right: 36px; top: 48px;
    font-size: 26px;
    color: var(--card-blue-deep);
  }

  .contact {
    position: absolute;
    left: 40px;
    bottom: 36px;
    color: var(--ink-white);
    font-size: 13px;
    line-height: 1.35;
  }
  .contact__name {
    font-weight: 700;
    font-size: 17px;
    text-transform: uppercase;
    letter-spacing: 0.5px;
  }
  .contact__role { margin-bottom: 14px; }
  .contact__address { margin-bottom: 12px; }
  .contact__line {
    display: flex;
    align-items: center;
    gap: 8px;
  }
  .contact__icon { width: 12px; height: 12px; flex: none; }
</style>
</head>
<body>
<main class="canvas">
  <section class="card card--front" aria-label="Card front">
    <div class="brand-name">Orbit Building Co</div>
  </section>

  <section class="card card--back" aria-label="Card back">
    <div class="brand-name">Orbit Building Co</div>

    <div class="contact">
      <div class="contact__name">Dario Lentz</div>
      <div class="contact__role">Founder &amp; CEO</div>
      <div class="contact__address">48 Fernhill Rd,<br>Ashmont, VIC 3290</div>
      <div class="contact__line">
        <svg class="contact__icon" viewBox="0 0 12 12" aria-hidden="true"><path d="M2.5 1 L4.5 1 L5.2 3.5 L4 4.6 Q5 7 7.4 8 L8.5 6.8 L11 7.5 L11 9.5 Q10.5 11 9 11 Q1 10 1 3 Q1 1.5 2.5 1 Z" fill="#fff"/></svg>
        <span>0400 555 018</span>
      </div>
      <div class="contact__line">
        <svg class="contact__icon" viewBox="0 0 12 12" aria-hidden="true"><rect x="0.5" y="2" width="11" height="8" rx="1" fill="#fff"/><path d="M1 2.6 L6 6.5 L11 2.6" fill="none" stroke="#2f6db5" stroke-width="1"/></svg>
        <span>info@orbitbuildingco.com.au</span>
      </div>
      <div class="contact__line">
        <svg class="contact__icon" viewBox="0 0 12 12" aria-hidden="true"><circle cx="6" cy="6" r="5.5" fill="#fff"/><path d="M0.5 6 H11.5 M6 0.5 Q3 6 6 11.5 M6 0.5 Q9 6 6 11.5" fill="none" stroke="#2f6db5" stroke-width="0.8"/></svg>
        <span>www.orbitbuildingco.com.au</span>
      </div>
    </div>
  </section>
</main>
</body>
</html>
```